Swimming Pool Supply Company Business Cards

We need business cards designed for company. These need to be easy to edit so that we can fill in names, titles, and contact info for each person who works here.

Dalton R. Whitfield
Manager of Legal & Finance
K.L. Brisbane, Incorporated

4837 Grenway Avenue
Marlow Heights, PA 19243

E. dalton@klbrisbane-example.com
M. (215) 555-0173
O. (215) 555-0148

Contact Information for Business Card

Looking to upgrade current business cards with graphic that can be edited. Looking for fresh ideas for an age old industry.

Font styles to use
Serif
Sans Serif

Colors

Designer to choose colors to be used in the design.

Requirements
Must have
• Professional, fresh, unique but professional

```html
<!DOCTYPE html>
<html lang="en">
<head>
<meta charset="utf-8">
<title>K.L. Brisbane Business Cards</title>
<link rel="stylesheet" href="https://fonts.googleapis.com/css2?family=Arimo:wght@400;700&family=Tinos:wght@700&display=swap">
<style>
  :root {
    --teal: #1fb5c4;
    --black: #0b0b0c;
    --white: #ffffff;
    --ink: #1a1a1a;
    --grey-text: #2b2b2b;
    --stage: #e9ebec;
  }
  * { box-sizing: border-box; margin: 0; padding: 0; }
  html, body { width: 1200px; height: 800px; overflow: hidden; }
  body {
    background: var(--stage);
    font-family: "Arimo", Arial, sans-serif;
    position: relative;
  }
  .card {
    position: absolute;
    top: 252px;
    width: 520px;
    height: 297px;
    overflow: hidden;
    box-shadow: 0 10px 28px rgba(0,0,0,.18);
  }
  .card--front { left: 60px; background: var(--white); }
  .card--back  { left: 620px; background: var(--black); }

  .front-art { position: absolute; inset: 0; width: 100%; height: 100%; }

  .person { position: absolute; left: 34px; top: 30px; }
  .person__name {
    font-family: "Arimo", Arial, sans-serif;
    font-weight: 700;
    font-size: 34px;
    line-height: 1;
    color: var(--teal);
    letter-spacing: .2px;
  }
  .person__title {
    font-family: "Tinos", "Times New Roman", serif;
    font-weight: 700;
    font-size: 15px;
    color: var(--ink);
    margin-top: 4px;
  }
  .contacts { position: absolute; left: 38px; top: 100px; list-style: none; }
  .contacts__item {
    display: flex; align-items: center; gap: 14px;
    height: 25px;
    font-size: 15px;
    color: var(--grey-text);
  }
  .contacts__icon { width: 16px; height: 16px; flex: none; }

  .front-brand {
    position: absolute;
    right: 20px; bottom: 30px;
    font-weight: 700;
    font-size: 20px;
    letter-spacing: 1px;
    color: var(--teal);
  }

  .back-brand {
    position: absolute;
    left: 0; right: 0; top: 92px;
    text-align: center;
    font-weight: 700;
    font-size: 66px;
    letter-spacing: 2px;
    color: var(--teal);
  }
  .back-tagline {
    position: absolute;
    left: 0; right: 0; top: 206px;
    text-align: center;
    font-weight: 700;
    font-size: 13px;
    color: var(--white);
  }
  .back-web {
    position: absolute;
    left: 0; right: 0; top: 226px;
    text-align: center;
    font-size: 11px;
    color: var(--white);
  }
  .back-web span { color: var(--teal); }
</style>
</head>
<body>

<section class="card card--front" aria-label="Business card front">
  <svg class="front-art" viewBox="0 0 520 297" preserveAspectRatio="none" aria-hidden="true">
    <path d="M0 246 C160 300 340 230 520 92 L520 106 C340 246 160 312 0 258 Z" fill="var(--teal)"/>
    <path d="M0 262 C160 314 340 250 520 112 L520 297 L0 297 Z" fill="var(--black)"/>
  </svg>

  <div class="person">
    <h1 class="person__name">Dalton R. Whitfield</h1>
    <p class="person__title">Manager of Legal &amp; Finance</p>
  </div>

  <ul class="contacts">
    <li class="contacts__item">
      <svg class="contacts__icon" viewBox="0 0 16 16" aria-hidden="true"><path d="M4 1.5l2.3 3-1.4 1.6c.8 1.8 2.2 3.2 4 4l1.6-1.4 3 2.3-1.6 2.5C7 13 3 9 1.5 3.1z" fill="var(--teal)"/></svg>
      (215) 555-0148
    </li>
    <li class="contacts__item">
      <svg class="contacts__icon" viewBox="0 0 16 16" aria-hidden="true"><rect x="4" y="1" width="8" height="14" rx="1.5" fill="none" stroke="var(--teal)" stroke-width="1.6"/><circle cx="8" cy="12.3" r="1" fill="var(--teal)"/></svg>
      (215) 555-0173
    </li>
    <li class="contacts__item">
      <svg class="contacts__icon" viewBox="0 0 16 16" aria-hidden="true"><circle cx="8" cy="8" r="3" fill="none" stroke="var(--teal)" stroke-width="1.6"/><path d="M11 5v4.2c0 1.5 2.8 1.5 2.8-1.2A5.8 5.8 0 1 0 11 13" fill="none" stroke="var(--teal)" stroke-width="1.6"/></svg>
      dalton@klbrisbane-example.com
    </li>
    <li class="contacts__item">
      <svg class="contacts__icon" viewBox="0 0 16 16" aria-hidden="true"><g fill="none" stroke="var(--teal)" stroke-width="1.3"><circle cx="8" cy="8" r="6.5"/><ellipse cx="8" cy="8" rx="2.8" ry="6.5"/><path d="M1.5 8h13M2.5 4.8h11M2.5 11.2h11"/></g></svg>
      www.klbrisbane-example.com
    </li>
  </ul>

  <p class="front-brand">BRISBANE</p>
</section>

<section class="card card--back" aria-label="Business card back">
  <p class="back-brand">BRISBANE</p>
  <p class="back-tagline">Big Enough to Serve You, Small Enough to Care</p>
  <p class="back-web">www.<span>klbrisbane-example</span>.com</p>
</section>

</body>
</html>
```